Design for web app with Plinkora Stratum Craft - Tarvo7 SMS consult

We are developing a web app that will work in browsers. Its main purpose is to allow for users (signing up and logging in with their phone number) to track their habbits and select consultants to whom they can send SMS for help.

The wireframes of the app can be accessed here (pdf):
https://files.plinkora.example/d/7K2mWqLzXv4NtRb9HcJpYsAeUfDg3/view

NB!: Please do not follow the mockups 100% literally, but the Plinkora Stratum craft guidelines.

The technical specifications and descriptions of the web app's functionalities are available in the link below:
https://papers.plinkora.example/doc/4HsTnV8bQeZr2LmXwYcKpDjAuFgN6oRiE5tW1yMx/edit

Requirements for the design:

- The design should be provided as PSD, where each page/section should be in its own PSD file OR all pages/sections should be represented as folder groups in a single PSD file.

- All graphical elements in the design should be delivered as single layers which can then be extracted from the PSD.

- All graphical elements (icons, graphical buttons, etc.) should be provided as vector objects in the PSD, so that they can be exported into different sizes without loss of quality (for responsiveness).

- The design should use either web safe fonts or Plinkora Type.

Instructions for the design:
The design should be based on Plinkora Stratum Craft - http://www.plinkora.example/craft/spec/stratum-craft/overview.html

Please also provide an app icon and suggest a logo for the app.

Requirements
Must have
• Based on Plinkora Stratum Craft
• Flat
Nice to have
• Nice looking and not so stiff as the default Plinkora Stratum Craft, but it is important to follow their guidelines.
Should not have
• 3D

```html
<!DOCTYPE html>
<html lang="en">
<head>
<meta charset="utf-8">
<title>Tarvo7 – SMS consult app screens</title>
<link rel="stylesheet" href="https://fonts.googleapis.com/css2?family=Titillium+Web:wght@300;400;600&family=Open+Sans:wght@300;400;600&display=swap">
<style>
  :root {
    --stage-blue: #0a5fae;
    --stage-blue-deep: #064a8c;
    --stage-top: #0b4f93;
    --app-dark: #262b33;
    --app-dark-2: #2d333c;
    --brand-blue: #1a6fad;
    --sky: #3aa8dc;
    --lime: #b8e000;
    --lime-edge: #8fae00;
    --orange: #f05a22;
    --orange-edge: #c4441a;
    --teal: #2fbf9a;
    --list-bg: #eeeff1;
    --icon-grey: #b4b8bd;
    --text-grey: #7c8188;
    --white: #ffffff;
    --cta-orange: #f05a28;
  }
  * { box-sizing: border-box; margin: 0; padding: 0; }
  html, body { width: 1200px; height: 1146px; overflow: hidden; }
  body { position: relative; background: var(--white); font-family: "Open Sans", Arial, sans-serif; }

  .stage {
    position: absolute; left: 0; top: 0; width: 1200px; height: 995px;
    background: radial-gradient(ellipse at 50% 45%, #1476c9 0%, var(--stage-blue) 45%, var(--stage-blue-deep) 100%);
  }
  .stage-header {
    position: absolute; left: 0; top: 0; width: 1200px; height: 175px;
    background: var(--stage-top);
  }
  .brand { position: absolute; display: flex; align-items: center; gap: 10px; }
  .brand-mark { width: 14px; height: 14px; background: var(--sky); }
  .brand-name { font-family: "Titillium Web", Arial, sans-serif; font-weight: 600; color: var(--white); letter-spacing: 1px; }
  .stage-header .brand { left: 48px; top: 62px; }
  .stage-header .brand-name { font-size: 34px; }

  .screen {
    position: absolute; top: 290px; width: 210px; height: 480px;
    background: var(--app-dark); overflow: hidden;
    display: flex; flex-direction: column;
  }
  .screen .brand-name { font-size: 20px; }
  .screen .brand-mark { width: 10px; height: 10px; }

  .app-bar { height: 44px; background: var(--app-dark); display: flex; align-items: center; justify-content: center; }
  .app-bar .brand-name { font-size: 13px; }
  .app-bar .brand-mark { width: 7px; height: 7px; }
  .title-bar {
    height: 40px; background: var(--sky); color: var(--white);
    font-size: 11px; text-transform: uppercase; letter-spacing: .5px;
    display: flex; align-items: center; justify-content: space-between; padding: 0 14px;
  }
  .title-bar.centered { justify-content: center; }

  /* consultant list */
  .consultant-list { background: var(--list-bg); padding: 6px 0; flex: 1; list-style: none; }
  .consultant { display: flex; height: 33px; margin-bottom: 0; }
  .consultant-icon { width: 28px; display: flex; align-items: center; justify-content: center; }
  .consultant-name {
    flex: 1; background: var(--white); margin: 2px 0; font-size: 10.5px; color: #555a61;
    display: flex; align-items: center; padding-left: 10px;
  }

  .btn {
    height: 38px; display: flex; align-items: center; justify-content: center;
    color: var(--white); font-size: 11px; text-transform: uppercase; letter-spacing: .5px;
  }
  .btn-lime { background: var(--lime); color: #3b4500; border-bottom: 3px solid var(--lime-edge); }
  .btn-blue { background: var(--brand-blue); border-bottom: 3px solid #0f5185; }
  .btn-orange { background: var(--orange); border-bottom: 3px solid var(--orange-edge); }
  .list-screen .btn-lime { margin: 8px 6px 10px; }

  /* forms */
  .form { padding: 0 16px; display: flex; flex-direction: column; gap: 8px; }
  .field { height: 38px; background: var(--white); display: flex; align-items: center; }
  .field-icon { width: 32px; height: 100%; display: flex; align-items: center; justify-content: center; border-right: 1px solid #e1e3e6; }
  .field-text { font-size: 10.5px; color: #a3a8ae; padding-left: 10px; }
  .login-screen .brand { position: static; margin: 64px 0 0 26px; }
  .login-screen .form { margin-top: 118px; }
  .link-muted { margin-top: 26px; text-align: center; font-size: 9.5px; color: var(--text-grey); text-transform: uppercase; letter-spacing: .5px; }

  .splash-screen { background: var(--app-dark-2); align-items: center; }
  .splash-screen .brand { position: static; margin-top: 196px; }
  .splash-screen .brand-name { font-size: 26px; }
  .splash-foot { margin-top: auto; margin-bottom: 26px; padding: 0 12px; text-align: center; color: #9aa0a8; }
  .splash-foot .copyright { font-size: 8px; text-transform: uppercase; margin-bottom: 8px; }
  .splash-foot .fine { font-size: 6.5px; line-height: 1.35; }

  .register-screen .brand { position: static; margin: 64px 0 0 26px; }
  .screen-heading {
    margin-top: 92px; text-align: center; color: #e4e6e9;
    font-family: "Titillium Web", Arial, sans-serif; font-weight: 300; font-size: 19px; letter-spacing: 1px;
  }
  .register-screen .form { margin-top: 14px; }

  /* daily check screen */
  .check-screen { background: var(--white); }
  .check-body { background: #f1f2f4; flex: 1; padding: 10px 6px; display: flex; flex-direction: column; }
  .vote-row { display: flex; height: 44px; }
  .vote { flex: 1; display: flex; align-items: center; justify-content: center; }
  .vote-up { background: var(--teal); }
  .vote-down { background: var(--orange); }
  .note-field { margin-top: 8px; height: 30px; background: var(--white); font-size: 10px; color: #6d7278; display: flex; align-items: center; padding-left: 10px; }
  .note-area { margin-top: 12px; flex: 1; background: var(--white); }
  .check-screen .btn-lime { margin-top: 10px; }

  .cta {
    position: absolute; left: 0; top: 1056px; width: 1200px; text-align: center;
    font-family: "Titillium Web", Arial, sans-serif; font-size: 29px; color: var(--cta-orange);
  }
</style>
</head>
<body>
  <section class="stage">
    <header class="stage-header">
      <div class="brand"><span class="brand-name">Tarvo7</span><span class="brand-mark"></span></div>
    </header>

    <!-- consultant selection -->
    <article class="screen list-screen" style="left:31px; background:var(--list-bg);">
      <div class="app-bar"><div class="brand"><span class="brand-name">Tarvo7</span><span class="brand-mark"></span></div></div>
      <div class="title-bar">Select your consultant</div>
      <ul class="consultant-list">
        <li class="consultant"><span class="consultant-icon"><svg width="11" height="12" viewBox="0 0 11 12"><circle cx="5.5" cy="3.2" r="3" fill="#b4b8bd"/><path d="M0 12c0-3.5 2.4-5.2 5.5-5.2S11 8.5 11 12z" fill="#b4b8bd"/></svg></span><span class="consultant-name">Lorian Pavek</span></li>
        <li class="consultant"><span class="consultant-icon"><svg width="11" height="12" viewBox="0 0 11 12"><circle cx="5.5" cy="3.2" r="3" fill="#b4b8bd"/><path d="M0 12c0-3.5 2.4-5.2 5.5-5.2S11 8.5 11 12z" fill="#b4b8bd"/></svg></span><span class="consultant-name">Dawid Halverin</span></li>
        <li class="consultant"><span class="consultant-icon"><svg width="11" height="12" viewBox="0 0 11 12"><circle cx="5.5" cy="3.2" r="3" fill="#b4b8bd"/><path d="M0 12c0-3.5 2.4-5.2 5.5-5.2S11 8.5 11 12z" fill="#b4b8bd"/></svg></span><span class="consultant-name">Chet Nollard</span></li>
        <li class="consultant"><span class="consultant-icon"><svg width="11" height="12" viewBox="0 0 11 12"><circle cx="5.5" cy="3.2" r="3" fill="#b4b8bd"/><path d="M0 12c0-3.5 2.4-5.2 5.5-5.2S11 8.5 11 12z" fill="#b4b8bd"/></svg></span><span class="consultant-name">Mira Fennick</span></li>
        <li class="consultant"><span class="consultant-icon"><svg width="11" height="12" viewBox="0 0 11 12"><circle cx="5.5" cy="3.2" r="3" fill="#b4b8bd"/><path d="M0 12c0-3.5 2.4-5.2 5.5-5.2S11 8.5 11 12z" fill="#b4b8bd"/></svg></span><span class="consultant-name">Kristof Brandel</span></li>
        <li class="consultant"><span class="consultant-icon"><svg width="11" height="12" viewBox="0 0 11 12"><circle cx="5.5" cy="3.2" r="3" fill="#b4b8bd"/><path d="M0 12c0-3.5 2.4-5.2 5.5-5.2S11 8.5 11 12z" fill="#b4b8bd"/></svg></span><span class="consultant-name">Zed Everly</span></li>
        <li class="consultant"><span class="consultant-icon"><svg width="11" height="12" viewBox="0 0 11 12"><circle cx="5.5" cy="3.2" r="3" fill="#b4b8bd"/><path d="M0 12c0-3.5 2.4-5.2 5.5-5.2S11 8.5 11 12z" fill="#b4b8bd"/></svg></span><span class="consultant-name">Jhon Doe</span></li>
        <li class="consultant"><span class="consultant-icon"><svg width="11" height="12" viewBox="0 0 11 12"><circle cx="5.5" cy="3.2" r="3" fill="#b4b8bd"/><path d="M0 12c0-3.5 2.4-5.2 5.5-5.2S11 8.5 11 12z" fill="#b4b8bd"/></svg></span><span class="consultant-name">Cris Rowden</span></li>
      </ul>
      <div class="btn btn-lime">Continue</div>
    </article>

    <!-- log in -->
    <article class="screen login-screen" style="left:263px;">
      <div class="brand"><span class="brand-name">Tarvo7</span><span class="brand-mark"></span></div>
      <div class="form">
        <div class="field"><span class="field-icon"><svg width="9" height="14" viewBox="0 0 9 14"><rect x="0.75" y="0.75" width="7.5" height="12.5" rx="1.2" fill="none" stroke="#b4b8bd" stroke-width="1.5"/><rect x="3" y="10.5" width="3" height="1" fill="#b4b8bd"/></svg></span><span class="field-text">Phone number</span></div>
        <div class="field"><span class="field-icon"><svg width="10" height="13" viewBox="0 0 10 13"><path d="M2.5 6V4a2.5 2.5 0 0 1 5 0v2" fill="none" stroke="#b4b8bd" stroke-width="1.4"/><rect x="0.5" y="6" width="9" height="6.5" rx="1" fill="#b4b8bd"/></svg></span><span class="field-text">Password</span></div>
        <div class="btn btn-blue">Log in</div>
        <div class="btn btn-lime">Register</div>
      </div>
      <p class="link-muted">Forgot password?</p>
    </article>

    <!-- splash -->
    <article class="screen splash-screen" style="left:495px;">
      <div class="brand"><span class="brand-name">Tarvo7</span><span class="brand-mark"></span></div>
      <footer class="splash-foot">
        <p class="copyright">(C) 2015, Company here</p>
        <p class="fine">Lorem ipsum dolor sit amet, consectetuer adipiscing elit, sed diam nonummy nibh euismod tincidunt ut laoreet dolore magna aliquam erat volutpat.</p>
      </footer>
    </article>

    <!-- register -->
    <article class="screen register-screen" style="left:727px;">
      <div class="brand"><span class="brand-name">Tarvo7</span><span class="brand-mark"></span></div>
      <h2 class="screen-heading">REGISTER</h2>
      <div class="form">
        <div class="field"><span class="field-icon"><svg width="9" height="14" viewBox="0 0 9 14"><rect x="0.75" y="0.75" width="7.5" height="12.5" rx="1.2" fill="none" stroke="#b4b8bd" stroke-width="1.5"/><rect x="3" y="10.5" width="3" height="1" fill="#b4b8bd"/></svg></span><span class="field-text">Phone number</span></div>
        <div class="btn btn-blue">Sign up</div>
        <div class="btn btn-orange">Cancel</div>
      </div>
    </article>

    <!-- daily check -->
    <article class="screen check-screen" style="left:959px;">
      <div class="app-bar"><div class="brand"><span class="brand-name">Tarvo7</span><span class="brand-mark"></span></div></div>
      <div class="title-bar"><span>12 May 2015</span><svg width="8" height="12" viewBox="0 0 8 12"><path d="M1.5 1l5 5-5 5" fill="none" stroke="#fff" stroke-width="1.8"/></svg></div>
      <div class="check-body">
        <div class="vote-row">
          <span class="vote vote-up"><svg width="18" height="18" viewBox="0 0 18 18"><path d="M1 8h3v9H1zM6 8l3.5-6.5c1.5 0 2 1 1.6 2.5L10.5 7H16a1.5 1.5 0 0 1 1.4 1.9l-2 7A1.5 1.5 0 0 1 14 17H6z" fill="none" stroke="#fff" stroke-width="1.4" stroke-linejoin="round"/></svg></span>
          <span class="vote vote-down"><svg width="18" height="18" viewBox="0 0 18 18"><path d="M1 1h3v9H1zM6 10l3.5 6.5c1.5 0 2-1 1.6-2.5L10.5 11H16a1.5 1.5 0 0 0 1.4-1.9l-2-7A1.5 1.5 0 0 0 14 1H6z" fill="none" stroke="#fff" stroke-width="1.4" stroke-linejoin="round"/></svg></span>
        </div>
        <div class="note-field">Describe your current situation</div>
        <div class="note-area"></div>
        <div class="btn btn-lime">Gem</div>
      </div>
    </article>
  </section>

  <p class="cta">Follow the link for more details</p>
</body>
</html>
```